Kestrel Garment Company "Sale Flyer"

We need flyer for a company selling clothing, the purpose of the flyer is advertising the available product. This flyer has to be specific for the product category of "men shorts". The flyer should be attractive and will have to feature pictures of the product which are attached. Furthermore, the flyer should feature the company name and logo. The company name is Kestrel Garment Company. The flyer should mention that the product is manufactured in a facility rated Platinum under the VORA Eco Structure Grading Scheme hence the damage to the environment is nill because of the product.The flyer should mention the address of the store No. 52, Fourth Lane Road, Colombo 11, Sri Lanka. The telephone number +94 71 508 3947. The product price also should be mentioned prominently which is "Rs. 790". Flyer size should be A4 front only. Many pictures are attached of course all cannot be used, looking forward to an attractive flyer. Thank you.

Target Market(s)

Men age 16 - 45

Industry/Entity Type

Clothing

Requirements
Must have
• Logo : in the attachment
• Contact number : +94 71 508 3947
• Address : No. 52, Fourth Lane Road, Colombo 11, Sri Lanka.
• Price : Rs. 790

```html
<!DOCTYPE html>
<html lang="en">
<head>
<meta charset="UTF-8">
<title>Kestrel Garment Company – Men Shorts Flyer</title>
<link href="https://fonts.googleapis.com/css2?family=Oswald:wght@500;700&family=Roboto:wght@400;700&family=Roboto+Condensed:wght@700&display=swap" rel="stylesheet">
<style>
  :root {
    --ink-dark: #2b2b2d;
    --ink-mid: #4a4a4d;
    --ink-soft: #6f6f72;
    --paper: #ffffff;
    --paper-grey: #ececec;
    --brand-red: #e3202a;
    --short-red: #e8333b;
    --short-steel: #8e9dc6;
    --short-cyan: #3fb7e6;
    --short-blue: #2566c9;
    --short-navy: #3b4356;
    --short-plaid: #a5a8ad;
    --short-sky: #5b8fc2;
    --short-indigo: #3d4f86;
  }
  html, body { margin: 0; padding: 0; overflow: hidden; background: var(--paper); }
  .flyer {
    position: relative;
    width: 889px;
    height: 1200px;
    overflow: hidden;
    background: var(--paper);
    font-family: "Roboto", sans-serif;
  }
  .flyer-backdrop { position: absolute; inset: 0; }
  .headline {
    position: absolute;
    left: 42px;
    top: 48px;
    font-family: "Oswald", sans-serif;
    line-height: 0.95;
    margin: 0;
  }
  .headline-men { display: block; color: var(--brand-red); font-size: 104px; font-weight: 700; }
  .headline-shorts { display: block; color: var(--paper); font-size: 74px; font-weight: 500; letter-spacing: 2px; }
  .brand-mark {
    position: absolute;
    left: 596px;
    top: 92px;
    width: 48px;
    height: 48px;
    background: var(--ink-mid);
  }
  .brand-name {
    position: absolute;
    left: 660px;
    top: 88px;
    margin: 0;
    font-family: "Roboto", sans-serif;
    font-weight: 700;
    font-size: 28px;
    line-height: 1.1;
    color: var(--ink-mid);
  }
  .product-shot { position: absolute; border-radius: 10px; }
  .shot-red { left: 395px; top: 168px; width: 165px; height: 175px; background: linear-gradient(160deg, #f0525a, var(--short-red)); }
  .shot-steel { left: 345px; top: 315px; width: 170px; height: 150px; background: linear-gradient(160deg, #a6b3d6, var(--short-steel)); }
  .shot-cyan { left: 120px; top: 390px; width: 185px; height: 170px; background: linear-gradient(160deg, #6acbef, var(--short-cyan)); }
  .shot-blue { left: 40px; top: 510px; width: 175px; height: 185px; background: linear-gradient(160deg, #3b7ede, var(--short-blue)); }
  .price-badge { position: absolute; left: 650px; top: 305px; width: 220px; height: 220px; }
  .price-text {
    position: absolute; inset: 0;
    display: flex; flex-direction: column; align-items: center; justify-content: center;
    font-family: "Roboto Condensed", sans-serif; font-weight: 700; line-height: 0.95;
  }
  .price-currency { color: var(--paper); font-size: 56px; }
  .price-amount { color: var(--brand-red); font-size: 74px; }
  .claim {
    position: absolute;
    right: 36px;
    top: 600px;
    margin: 0;
    text-align: right;
    color: var(--ink-mid);
    font-size: 37px;
    line-height: 1.3;
  }
  .claim-scheme {
    position: absolute;
    left: 0; right: 0;
    top: 735px;
    margin: 0;
    text-align: center;
    font-family: "Roboto Condensed", sans-serif;
    font-weight: 700;
    font-size: 44px;
    color: var(--ink-dark);
  }
  .claim-tail {
    position: absolute;
    left: 0; right: 0;
    top: 795px;
    margin: 0;
    text-align: center;
    font-size: 28px;
    color: var(--ink-mid);
  }
  .swatch { position: absolute; width: 160px; height: 160px; border-radius: 50%; top: 850px; }
  .swatch-ring { position: absolute; width: 174px; height: 174px; border-radius: 50%; top: 843px; border: 2px dashed var(--ink-soft); box-sizing: border-box; }
  .ring-1 { left: 40px; } .ring-2 { left: 255px; } .ring-3 { left: 470px; } .ring-4 { left: 685px; }
  .swatch-navy { left: 47px; background: radial-gradient(circle, #4a5368, var(--short-navy)); }
  .swatch-plaid { left: 262px; background: radial-gradient(circle, #c2c5c9, var(--short-plaid)); }
  .swatch-sky { left: 477px; background: radial-gradient(circle, #78a6d2, var(--short-sky)); }
  .swatch-indigo { left: 692px; background: radial-gradient(circle, #50639c, var(--short-indigo)); }
  .contact {
    position: absolute;
    left: 0; right: 0;
    top: 1036px;
    text-align: center;
    color: var(--ink-dark);
  }
  .contact-line { margin: 0; display: flex; justify-content: center; align-items: center; gap: 8px; }
  .contact-address { font-size: 24px; }
  .contact-phone { font-size: 32px; font-weight: 700; margin-top: 4px; }
  .contact-icon { width: 24px; height: 24px; fill: var(--brand-red); }
</style>
</head>
<body>
<div class="flyer">
  <svg class="flyer-backdrop" width="889" height="1200" viewBox="0 0 889 1200" aria-hidden="true">
    <rect width="889" height="1200" fill="#ffffff"/>
    <polygon points="560,0 889,0 889,560" fill="#ececec"/>
    <polygon points="0,0 640,0 0,600" fill="#2b2b2d"/>
    <polygon points="0,600 640,0 700,0 0,660" fill="#3a3a3d"/>
    <path d="M0,1162 Q450,1130 889,1162 L889,1200 L0,1200 Z" fill="#e3202a"/>
    <path d="M0,1180 Q450,1155 889,1180 L889,1200 L0,1200 Z" fill="#2b2b2d"/>
  </svg>

  <h1 class="headline">
    <span class="headline-men">MEN</span>
    <span class="headline-shorts">SHORTS</span>
  </h1>

  <span class="brand-mark"></span>
  <p class="brand-name">Kestrel<br>Garment Company</p>

  <div class="product-shot shot-red" role="img" aria-label="Photo of red men's shorts"></div>
  <div class="product-shot shot-steel" role="img" aria-label="Photo of steel blue men's shorts"></div>
  <div class="product-shot shot-cyan" role="img" aria-label="Photo of cyan men's shorts"></div>
  <div class="product-shot shot-blue" role="img" aria-label="Photo of royal blue men's shorts"></div>

  <div class="price-badge">
    <svg width="220" height="220" viewBox="0 0 220 220" aria-hidden="true">
      <polygon fill="#2b2b2d" points="110,0 124,16 143,5 150,25 171,20 170,41 191,43 183,62 203,71 189,86 205,100 188,112 200,130 180,137 186,157 165,158 165,179 145,173 137,193 121,180 110,198 99,180 83,193 75,173 55,179 55,158 34,157 40,137 20,130 32,112 15,100 31,86 17,71 37,62 29,43 50,41 49,20 70,25 77,5 96,16"/>
    </svg>
    <div class="price-text">
      <span class="price-currency">Rs</span>
      <span class="price-amount">790</span>
    </div>
  </div>

  <p class="claim">The product is manufactured in a<br>facility rated Platinum under the</p>
  <p class="claim-scheme">VORA Eco Structure Grading Scheme</p>
  <p class="claim-tail">hence the damage to the environment is nill because of the product</p>

  <div class="swatch-ring ring-1"></div>
  <div class="swatch swatch-navy" role="img" aria-label="Close-up photo of charcoal shorts"></div>
  <div class="swatch-ring ring-2"></div>
  <div class="swatch swatch-plaid" role="img" aria-label="Close-up photo of grey check shorts"></div>
  <div class="swatch-ring ring-3"></div>
  <div class="swatch swatch-sky" role="img" aria-label="Close-up photo of sky blue shorts"></div>
  <div class="swatch-ring ring-4"></div>
  <div class="swatch swatch-indigo" role="img" aria-label="Close-up photo of indigo shorts"></div>

  <div class="contact">
    <p class="contact-line contact-address">
      <svg class="contact-icon" viewBox="0 0 24 24" aria-hidden="true"><path d="M12 2a7 7 0 0 0-7 7c0 5 7 13 7 13s7-8 7-13a7 7 0 0 0-7-7zm0 9.5A2.5 2.5 0 1 1 12 6.5a2.5 2.5 0 0 1 0 5z"/></svg>
      Store No. 52, Fourth Lane Road, Colombo 11, Sri Lanka.
    </p>
    <p class="contact-line contact-phone">
      <svg class="contact-icon" viewBox="0 0 24 24" aria-hidden="true"><path d="M6.6 10.8a15.1 15.1 0 0 0 6.6 6.6l2.2-2.2a1 1 0 0 1 1-.25 11.4 11.4 0 0 0 3.6.57 1 1 0 0 1 1 1V20a1 1 0 0 1-1 1A17 17 0 0 1 3 4a1 1 0 0 1 1-1h3.5a1 1 0 0 1 1 1c0 1.250.2 2.45.57 3.6a1 1 0 0 1-.25 1z"/></svg>
      +94 71 508 3947
    </p>
  </div>
</div>
</body>
</html>
```